Flyer Template Design

I have attached 4 files. I would like a design template that could be used across these documents so that they have a common look and feel. The content of the documents is tested and should not be changed significantly. The images can be changed. I have also attache our logo for color compatibility.
Updates

Need extra days to review

Target Market(s)

Wealthy Christian donors

Font styles to use
Serif
Sans Serif

```html
<!DOCTYPE html>
<html lang="en">
<head>
<meta charset="utf-8">
<title>The Final Lap – Flyer</title>
<link href="https://fonts.googleapis.com/css2?family=Archivo+Black&family=Libre+Baskerville:wght@400;700&family=Oswald:wght@600&family=Source+Sans+3:ital,wght@0,400;0,700;0,800;1,700;1,800&display=swap" rel="stylesheet">
<style>
  :root {
    --page-bg: #5a5a5a;
    --paper: #ffffff;
    --sky-blue: #2fa3da;
    --deep-blue: #0f5d92;
    --mid-blue: #2a8cc6;
    --band-grey: #d9d9d9;
    --green: #4ea81d;
    --green-text: #45a41c;
    --ink: #111111;
    --white: #ffffff;
  }
  * { box-sizing: border-box; margin: 0; padding: 0; }
  html, body { width: 1200px; height: 1200px; overflow: hidden; background: var(--page-bg); }
  .flyer {
    position: absolute; left: 194px; top: 30px;
    width: 753px; height: 1057px;
    transform: scale(1.0785); transform-origin: 0 0;
    background: var(--paper); overflow: hidden;
    font-family: "Source Sans 3", sans-serif; color: var(--ink);
  }
  .hero { position: absolute; left: 0; top: 0; width: 753px; height: 398px; }
  .hero-photo {
    position: absolute; inset: 0;
    background: linear-gradient(160deg, #4d5a66 0%, #3c4248 50%, #5a3a30 100%);
  }
  .hero-panel { position: absolute; inset: 0; }
  .brand { position: absolute; left: 40px; top: 50px; display: flex; align-items: center; gap: 20px; }
  .brand-mark { width: 46px; height: 46px; background: var(--white); }
  .brand-name {
    font-family: "Libre Baskerville", serif; font-weight: 400; color: var(--white);
    font-size: 24px; line-height: 27px; text-transform: uppercase;
  }
  .title-top {
    position: absolute; left: 28px; top: 168px;
    font-family: "Archivo Black", sans-serif; font-size: 86px; line-height: 1; color: var(--ink); letter-spacing: -1px;
  }
  .title-main {
    position: absolute; left: 28px; top: 250px;
    font-family: "Libre Baskerville", serif; font-weight: 700; font-size: 52px; line-height: 1; color: var(--white); white-space: nowrap;
  }
  .grey-band { position: absolute; left: 0; top: 398px; width: 753px; height: 22px; background: var(--band-grey); }
  .footer-band { position: absolute; left: 0; top: 1028px; width: 753px; height: 29px; background: var(--green); }
  .side-column {
    position: absolute; left: 0; top: 420px; width: 337px; height: 500px;
    background: linear-gradient(180deg, var(--deep-blue) 0%, var(--mid-blue) 55%, var(--sky-blue) 100%);
    border-top-right-radius: 32px;
  }
  .side-photo {
    position: absolute; left: 30px; top: 12px; width: 290px; height: 175px;
    border: 3px solid var(--white); border-radius: 20px;
    background: linear-gradient(180deg, #4f8fc6 0%, #8cb6d8 60%, #a9c7df 100%);
  }
  .side-copy { position: absolute; left: 30px; top: 202px; width: 295px; color: var(--white); }
  .side-heading { font-weight: 800; font-size: 22px; line-height: 1.1; margin-bottom: 6px; letter-spacing: -0.2px; }
  .side-copy p { font-size: 12.2px; line-height: 16.2px; text-align: justify; }
  .side-copy .side-lead { font-weight: 700; font-size: 14.5px; line-height: 1.2; margin: 8px 0 9px; text-align: left; }
  .cta {
    position: absolute; left: 0; top: 888px; width: 337px; height: 169px;
    background: var(--green); border-top-right-radius: 40px; color: var(--white);
    padding: 14px 20px 0 30px;
  }
  .cta-heading { font-family: "Oswald", sans-serif; font-weight: 600; font-size: 24px; line-height: 26px; text-transform: uppercase; letter-spacing: 0.3px; }
  .cta-contact { margin-top: 6px; font-size: 14.5px; line-height: 19px; }
  .cta-contact strong { font-weight: 700; letter-spacing: 0.3px; }
  .main-column {
    position: absolute; left: 337px; top: 420px; width: 416px; height: 608px;
    background: var(--paper); border-bottom-left-radius: 46px;
    padding: 16px 30px 0 25px;
  }
  .main-column p { font-size: 12.9px; line-height: 16.2px; text-align: justify; margin-bottom: 9px; }
  .main-column .section-heading { color: var(--green-text); font-weight: 800; font-size: 22px; line-height: 1.1; margin: 10px 0 5px; }
  .main-column .question { color: var(--green-text); font-style: italic; font-weight: 800; font-size: 14.5px; margin: 6px 0 6px; text-transform: uppercase; }
  .main-column .answer { font-style: italic; font-weight: 800; font-size: 14.5px; line-height: 19px; text-transform: uppercase; margin-bottom: 6px; text-align: justify; letter-spacing: 0.4px; }
  .main-column .answer em { color: var(--green-text); }
  .main-column .closing { color: var(--green-text); font-style: italic; font-weight: 800; font-size: 14.5px; line-height: 19px; text-transform: uppercase; letter-spacing: 0.3px; }
</style>
</head>
<body>
  <main class="flyer">
    <header class="hero">
      <div class="hero-photo" role="img" aria-label="Sprinter crouched at the starting line on a floodlit stadium track"></div>
      <svg class="hero-panel" width="753" height="398" viewBox="0 0 753 398" aria-hidden="true">
        <defs>
          <linearGradient id="panelFill" x1="0" y1="0" x2="0" y2="1">
            <stop offset="0" stop-color="#2fa6dc"/>
            <stop offset="0.6" stop-color="#2b9bd4"/>
            <stop offset="1" stop-color="#2a8fc8"/>
          </linearGradient>
        </defs>
        <polygon points="0,0 287,0 427,208 362,398 0,398" fill="url(#panelFill)"/>
      </svg>
      <div class="brand">
        <span class="brand-mark"></span>
        <span class="brand-name">The<br>Harvest<br>Fund</span>
      </div>
      <div class="title-top">THE</div>
      <h1 class="title-main">FINAL LAP</h1>
    </header>

    <div class="grey-band"></div>
    <div class="footer-band"></div>

    <section class="side-column">
      <div class="side-photo" role="img" aria-label="Runner breaking the finish line tape against a blue sky"></div>
      <div class="side-copy">
        <h2 class="side-heading">SPRINTING TO THE FINISH</h2>
        <p>In his second letter, the Apostle Peter instructs believers “to hasten the coming of the day of God.” As the end of the race draws near, he’s saying, we should sprint toward the finish line, striving to finish the race as quickly as we can.</p>
        <p class="side-lead">You can be part of the sprint to the finish.</p>
        <p>Partner with the Harvest Fund and finance the missionaries who are taking the gospel for the first time to those last remaining people groups. Your investment will “hasten the coming of the day of God” by accelerating the effort to “make disciples of every nation.” In 2018, our partners sent the gospel to 231 people groups in 35 countries.</p>
      </div>
    </section>

    <section class="cta">
      <h2 class="cta-heading">Join us as we invest to make disciples in “all nations” by 2022.</h2>
      <p class="cta-contact"><strong>To learn more, email Daniel Carter at</strong><br>dcarter@harvestfund.org.</p>
    </section>

    <article class="main-column">
      <p>Every four years, the Olympic Marathon is run through the streets of the host city. The final lap, though, is always run in the Olympic Stadium. At the end of the race, the runners burst into the stadium for the final lap, and the crowd explodes in celebration of a long race well run.</p>
      <p>For 2000 years, the church has been running a Marathon, racing to fulfill Jesus’ command to “make disciples of all nations.” But now we’re nearly done: we’ve come into the stadium; we’re on the final lap. And the heavenly crowd is standing and cheering!</p>
      <h2 class="section-heading">THE FINISH LINE</h2>
      <p>Jesus himself defined the finish line when he said, “This gospel of the kingdom will be preached in the whole world as a testimony to all nations, and then the end will come.”</p>
      <h3 class="question">When will the race end?</h3>
      <p class="answer">Jesus said, when the gospel has been proclaimed to <em>“all nations.”</em></p>
      <p>In the Bible, the word “nations” refers to people groups: groups of people who share a common ethnicity, culture, and language. Amazingly, there are about 12,000 of these “nations” around the world—and Jesus commanded us to make disciples in all of them!</p>
      <p>Today, there are still about 500 people groups around the world have never heard the gospel. Most of these remaining groups are small and located in remote, difficult places. But now that we know who and where they are, by God’s grace it is possible for us to engage every one of them with the gospel within the next 3 years.</p>
      <p class="closing">In other words, after a long race, we’re on the final lap!</p>
    </article>
  </main>
</body>
</html>
```